Website design for online service business

The company provides the following services:
1 - consultancy services on existing products (like teamvault and deskline 354)
2 - Coaching services - Coach someone on services like using/developing features with existing products, or teach how to be more productive, or improve their business using automation, etc
3 - Training
- Online training on demand on existing products via voxora (like in Teamvault and deskline 365)
- Online courses through videos lessons and scripts by offering information products where people will need to register and pay in advance to access the online course. (productivity courses for example)

- The goal is for clients to book time with me for one of those areas without too many clicks.
- Clients will be able to Book time using an integration (it would be good to have the layout integrated with the site.) with this https://planner.brellix.example/cal/BrightPathWorks1@brightpathworks.brellix.example/slots/

- there will be areas for which i whish to build a VIP mailing list. It's referenced on the wireframes

References:
https://www.ledgerandlanternhub.example/about/about-dorvin/
https://www.quillandcompass.example/
https://teamvaultsage.example/

Target Market(s)

- Small businesses
- Freelancers

Industry/Entity Type

Business

Number of Pages Required

5+ page

Font styles to use
Sans Serif

Colors

Designer to choose colors to be used in the design.

Requirements
Must have
• Must have the design optimized to the less clicks possible to achieve any action
• The colors of the site should follow the logo (provided in attach)
• It should use other color that belong to the same pallet of colors
• Should contain colors that incentivizes people to click and book something
• Images and backgrounds should be made available
• All images sizes and colors should be provided to be able to develop the site according to the design
Nice to have
• The bookings for the time should be integrated within the design. If not possible a redirection to it can work as well.
Should not have
• Links to social media
• Pop-ups
• Intrusive navigations (like navigation bares on the left or right hand side)
• Should not be a template used by many people

```html
<!DOCTYPE html>
<html lang="en">
<head>
<meta charset="utf-8">
<title>BrightPath Works – Home</title>
<link rel="stylesheet" href="https://fonts.googleapis.com/css2?family=Noto+Sans:wght@400;700&family=Open+Sans:wght@400;700&family=Comfortaa:wght@400&display=swap">
<style>
  :root {
    --brand-blue: #0a6fa3;
    --brand-blue-text: #1479ad;
    --accent-orange: #f7941d;
    --accent-orange-dark: #d97a0c;
    --section-sky: #d9f0fb;
    --ink: #333333;
    --ink-soft: #4a4a4a;
    --white: #ffffff;
    --hero-grey: #8c8c8c;
  }
  * { box-sizing: border-box; margin: 0; padding: 0; }
  html, body { width: 800px; height: 1200px; overflow: hidden; background: var(--white); }
  body { font-family: "Noto Sans", sans-serif; color: var(--ink); }
  .page { position: relative; width: 800px; height: 1200px; overflow: hidden; }

  .btn {
    position: absolute; display: flex; align-items: center; justify-content: center;
    font-family: "Open Sans", sans-serif; font-weight: 700; font-size: 10px;
    color: var(--white); text-decoration: none; letter-spacing: .3px;
    box-shadow: 1px 2px 2px rgba(0,0,0,.25);
  }
  .btn--orange { background: var(--accent-orange); border-bottom: 1px solid var(--accent-orange-dark); }
  .btn--blue { background: var(--brand-blue); }

  /* header */
  .site-header { position: absolute; top: 0; left: 0; width: 800px; height: 60px; background: var(--white); }
  .brand { position: absolute; left: 100px; top: 14px; display: flex; align-items: center; gap: 6px; }
  .brand__mark { width: 14px; height: 14px; background: var(--brand-blue); }
  .brand__name { font-family: "Noto Sans", sans-serif; font-weight: 700; font-size: 13px; color: var(--brand-blue); letter-spacing: 1px; line-height: 1.1; width: 80px; }
  .main-nav { position: absolute; left: 278px; top: 44px; display: flex; gap: 31px; font-size: 9.5px; letter-spacing: .3px; }
  .main-nav a { color: var(--ink); text-decoration: none; }
  .main-nav a.is-current { color: var(--brand-blue-text); }
  .btn--contact { left: 615px; top: 35px; width: 86px; height: 20px; }

  /* hero */
  .hero { position: absolute; top: 60px; left: 0; width: 800px; height: 250px; background: linear-gradient(180deg, #8a8a8a 0%, #9a9a98 55%, #b0b0a8 100%); }
  .hero__art { position: absolute; inset: 0; background: radial-gradient(ellipse 60px 70px at 354px 170px, #f4f4dc 0%, rgba(230,230,190,.5) 45%, rgba(0,0,0,0) 100%); }
  .hero__quote { position: absolute; left: 0; width: 800px; top: 30px; text-align: center; font-family: "Comfortaa", sans-serif; font-size: 30px; color: var(--white); }

  /* services */
  .services { position: absolute; top: 310px; left: 0; width: 800px; height: 300px; background: var(--section-sky); }
  .section-title { position: absolute; left: 0; width: 800px; text-align: center; font-size: 20px; font-weight: 400; color: var(--ink); }
  .services .section-title { top: 22px; }
  .service { position: absolute; top: 68px; width: 160px; text-align: center; }
  .service--teach { left: 82px; }
  .service--together { left: 319px; }
  .service--forme { left: 556px; }
  .service__icon { width: 56px; height: 52px; margin: 0 auto; border-radius: 4px; }
  .service__icon--board { background: #4f9a3c; }
  .service__icon--chat { background: #c7dce8; }
  .service__icon--desk { background: #b9cfdc; }
  .service__title { margin-top: 12px; font-size: 9.5px; font-weight: 700; letter-spacing: .5px; color: var(--ink); }
  .service__text { margin: 12px auto 0; width: 130px; font-size: 7.6px; line-height: 12px; color: var(--ink-soft); }
  .service .btn { position: relative; margin: 10px auto 0; width: 86px; height: 21px; }

  /* why */
  .why { position: absolute; top: 610px; left: 0; width: 800px; height: 266px; background: var(--white); }
  .why .section-title { top: 20px; }
  .why__photo { position: absolute; left: 100px; top: 69px; width: 290px; height: 172px; background: linear-gradient(135deg, #7d8a70 0%, #9a9a94 50%, #6d6b68 100%); }
  .why__copy { position: absolute; left: 412px; top: 68px; width: 292px; font-size: 7.6px; line-height: 12px; color: var(--ink-soft); }
  .why__copy p + p { margin-top: 7px; }
  .btn--more { left: 412px; top: 221px; width: 86px; height: 20px; }

  /* questions */
  .questions { position: absolute; top: 876px; left: 0; width: 800px; height: 275px; background: var(--section-sky); text-align: center; }
  .questions .section-title { top: 20px; }
  .questions__art { position: absolute; left: 142px; top: 72px; width: 126px; height: 124px; border-radius: 50%; background: rgba(255,255,255,.35); }
  .questions__lead { position: absolute; top: 56px; left: 0; width: 800px; font-size: 8.6px; color: var(--ink); }
  .questions__list { position: absolute; top: 73px; left: 0; width: 800px; list-style: none; font-size: 8.6px; color: var(--ink); }
  .questions__list li { height: 21.5px; line-height: 12px; }
  .questions__dots { display: block; color: var(--accent-orange); font-size: 8px; line-height: 8px; letter-spacing: 1px; font-weight: 700; }
  .questions__reassure { position: absolute; top: 164px; left: 0; width: 800px; font-size: 15px; color: var(--brand-blue-text); }
  .questions__here { position: absolute; top: 186px; left: 0; width: 800px; font-size: 8.6px; }
  .questions__book { position: absolute; top: 200px; left: 0; width: 800px; font-size: 8.6px; }
  .questions__note { position: absolute; top: 214px; left: 0; width: 800px; font-size: 6px; color: var(--ink-soft); }
  .btn--book { left: 357px; top: 232px; width: 86px; height: 21px; }

  /* footer */
  .site-footer { position: absolute; top: 1151px; left: 0; width: 800px; height: 49px; background: var(--brand-blue); color: var(--white); }
  .site-footer__copy { position: absolute; left: 100px; top: 18px; font-family: "Open Sans", sans-serif; font-weight: 700; font-size: 7.5px; }
  .site-footer__brand { position: absolute; left: 360px; top: 12px; width: 80px; text-align: center; font-weight: 700; font-size: 10px; letter-spacing: 1px; line-height: 1.15; }
  .footer-nav { position: absolute; right: 100px; top: 18px; display: flex; gap: 9px; font-family: "Open Sans", sans-serif; font-weight: 700; font-size: 8px; }
  .footer-nav a { color: var(--white); text-decoration: none; }
</style>
</head>
<body>
<div class="page">

  <header class="site-header">
    <div class="brand">
      <span class="brand__mark"></span>
      <span class="brand__name">BRIGHTPATH WORKS</span>
    </div>
    <nav class="main-nav">
      <a href="#" class="is-current">HOME</a>
      <a href="#">SERVICES</a>
      <a href="#">BLOG</a>
      <a href="#">ABOUT ME</a>
    </nav>
    <a href="#" class="btn btn--orange btn--contact">CONTACT ME</a>
  </header>

  <section class="hero">
    <div class="hero__art" role="img" aria-label="Row of light bulbs with one glowing bulb in the middle"></div>
    <p class="hero__quote">"...because ideas are a million"</p>
  </section>

  <section class="services">
    <h2 class="section-title">How can I help you with your idea?</h2>

    <div class="service service--teach">
      <div class="service__icon service__icon--board" role="img" aria-label="Illustration of a green chalkboard listing course topics"></div>
      <h3 class="service__title">I WILL TEACH YOU</h3>
      <p class="service__text">I want to learn at my own pace. You teach me how things are done and how it works and I will do it myself.</p>
      <a href="#" class="btn btn--orange">TEACH ME</a>
    </div>

    <div class="service service--together">
      <div class="service__icon service__icon--chat" role="img" aria-label="Illustration of two people sharing ideas in speech bubbles"></div>
      <h3 class="service__title">WE DO IT TOGETHER</h3>
      <p class="service__text">I want to learn how it workswand want to do it but I need someone that works along side with me.</p>
      <a href="#" class="btn btn--orange">LET'S DO IT</a>
    </div>

    <div class="service service--forme">
      <div class="service__icon service__icon--desk" role="img" aria-label="Illustration of a person working at a laptop with an idea bulb"></div>
      <h3 class="service__title">I'LL DO IT FOR YOU</h3>
      <p class="service__text">I have this great idea butI just want to have it done for me. I don't wont to do it or even learn about it.</p>
      <a href="#" class="btn btn--orange">DO IT FOR ME</a>
    </div>
  </section>

  <section class="why">
    <h2 class="section-title">Why should you hire my services?</h2>
    <div class="why__photo" role="img" aria-label="Portrait photo of the consultant outdoors on a residential street"></div>
    <div class="why__copy">
      <p>Lorem ipsum dolor sit amet, consectetur adipisicing elit, sed do eiusmod tempor incididunt ut labore et dolore magna aliqua. Ut enim ad minim veniam, quis nostrud exercitation ullamco laboris nisi ut aliquip ex ea commodo consequat. Duis aute irure dolor in reprehenderit in voluptate velit esse cillum dolore eu fugiat nulla pariatur. Excepteur sint occaecat cupidatat non proident, sunt in culpa qui officia deserunt mollit anim id est laborum. Sed ut perspiciatis unde omnis iste natus error sit voluptatem accusantium doloremque laudantium, totam rem aperiam, eaque ipsa quae ab illo inventore veritatis et quasi architecto beatae vitae dicta sunt explicabo.</p>
      <p>Neque porro quisquam est, qui dolorem ipsum.</p>
    </div>
    <a href="#" class="btn btn--blue btn--more">READ MORE</a>
  </section>

  <section class="questions">
    <div class="questions__art" role="img" aria-label="Faint sketched speech bubble with a question mark"></div>
    <h2 class="section-title">Do you have any questions?</h2>
    <p class="questions__lead">It's ok if you have questions.We haven't worked together or meath each other so how do you now if:</p>
    <ul class="questions__list">
      <li>We can work together?<span class="questions__dots">•••</span></li>
      <li>Understand each other?<span class="questions__dots">•••</span></li>
      <li>(Did I say work together?)<span class="questions__dots">•••</span></li>
      <li>I have the experience you are looking for?</li>
    </ul>
    <p class="questions__reassure">Don't worry about anything.</p>
    <p class="questions__here">I'm here for you!</p>
    <p class="questions__book">Use the button bellow to book a time slot where we can have a chat about what you need help with and we will take it from there.</p>
    <p class="questions__note">With coffee included ofcourse!</p>
    <a href="#" class="btn btn--orange btn--book">BOOK ME!</a>
  </section>

  <footer class="site-footer">
    <p class="site-footer__copy">Copyright @ 2018 BrightPathWorks. All rights reserved.</p>
    <div class="site-footer__brand">BRIGHTPATH WORKS</div>
    <nav class="footer-nav">
      <a href="#">Home</a>
      <a href="#">Services</a>
      <a href="#">Blog</a>
      <a href="#">About me</a>
      <a href="#">Contact me</a>
    </nav>
  </footer>

</div>
</body>
</html>
```